Redesign of Business Cards to Update them!

We want a full overhaul of our business cards! We have a design that is almost 5 years old and it needs to be updated to be current

Address is 437 Dunmore Lane Suite 12 Brenwick CA 90417
PH: 5554718263
Zorlivo.com

Hours M-F 10AM-4PM
Sat and Sunday Closed

```html
<!DOCTYPE html>
<html lang="en">
<head>
<meta charset="UTF-8">
<title>Zorlivo Business Cards</title>
<link href="https://fonts.googleapis.com/css2?family=Montserrat:wght@400;500&family=Poppins:wght@800&display=swap" rel="stylesheet">
<style>
  :root {
    --brand-red: #ec1c24;
    --ink: #111111;
    --text: #2a2a2a;
    --paper: #ffffff;
    --backdrop: #efefef;
    --icon-ring: #888888;
  }
  * { margin: 0; padding: 0; box-sizing: border-box; }
  html, body { width: 1200px; height: 1200px; overflow: hidden; }
  body {
    background: var(--backdrop);
    font-family: "Montserrat", sans-serif;
    position: relative;
  }
  .card {
    position: absolute;
    width: 640px;
    height: 366px;
    background: var(--paper);
    box-shadow: 0 14px 30px rgba(0,0,0,0.18);
    overflow: hidden;
  }
  .card--front { left: 80px; top: 170px; }
  .card--back { left: 480px; top: 650px; }

  .card__band {
    position: absolute;
    left: 0; bottom: 0;
    width: 100%;
    height: 20px;
  }

  .brand-name {
    font-family: "Poppins", sans-serif;
    font-weight: 800;
    color: var(--ink);
    letter-spacing: 0.5px;
  }

  /* Front */
  .front__brand {
    position: absolute;
    left: 58px; top: 138px;
    font-size: 34px;
  }
  .front__details {
    position: absolute;
    left: 238px; top: 88px;
    color: var(--text);
  }
  .holder-name {
    margin-left: 40px;
    color: var(--brand-red);
    font-size: 19px;
    font-weight: 400;
    letter-spacing: 0.3px;
  }
  .holder-role {
    margin-left: 40px;
    font-size: 15px;
    letter-spacing: 4px;
    margin-top: 2px;
  }
  .contact-list { list-style: none; margin-top: 22px; }
  .contact-item {
    display: flex;
    align-items: flex-start;
    gap: 18px;
    font-size: 15px;
    line-height: 20px;
    margin-bottom: 9px;
  }
  .contact-item--address { margin-top: 30px; }
  .contact-icon { width: 21px; height: 21px; flex: none; }
  .contact-item span { display: block; }

  /* Back */
  .back__brand {
    position: absolute;
    left: 0; width: 100%;
    top: 118px;
    text-align: center;
    font-size: 56px;
  }
  .back__site {
    position: absolute;
    right: 46px; top: 274px;
    display: flex; align-items: center; gap: 6px;
    color: var(--brand-red);
    font-size: 25px;
  }
  .back__site svg { width: 22px; height: 22px; }
</style>
</head>
<body>

<section class="card card--front" aria-label="Business card front">
  <div class="front__brand brand-name">Zorlivo</div>

  <div class="front__details">
    <h1 class="holder-name">DEVAN RATHORE</h1>
    <p class="holder-role">OWNER</p>
    <ul class="contact-list">
      <li class="contact-item">
        <svg class="contact-icon" viewBox="0 0 24 24" aria-hidden="true">
          <circle cx="12" cy="12" r="10.5" fill="none" stroke="var(--icon-ring)" stroke-width="1"/>
          <path d="M8.5 7c.6-.5 1.2-.4 1.6.2l1 1.6c.3.5.2 1-.2 1.4l-.6.5c.5 1.2 1.5 2.3 2.8 2.9l.5-.6c.4-.4 1-.5 1.4-.2l1.6 1c.6.4.7 1 .2 1.6-.8 1-2 1.3-3.2.8-2.6-1.1-4.6-3.1-5.7-5.7-.5-1.2-.2-2.5.6-3.5z" fill="var(--brand-red)"/>
        </svg>
        <span>PH: 5554718263</span>
      </li>
      <li class="contact-item">
        <svg class="contact-icon" viewBox="0 0 24 24" aria-hidden="true">
          <circle cx="12" cy="12" r="10.5" fill="none" stroke="var(--icon-ring)" stroke-width="1"/>
          <g fill="none" stroke="var(--brand-red)" stroke-width="0.9">
            <circle cx="12" cy="12" r="5.5"/>
            <ellipse cx="12" cy="12" rx="2.5" ry="5.5"/>
            <line x1="6.5" y1="12" x2="17.5" y2="12"/>
            <line x1="7.2" y1="9.3" x2="16.8" y2="9.3"/>
            <line x1="7.2" y1="14.7" x2="16.8" y2="14.7"/>
          </g>
        </svg>
        <span>Zorlivo.com</span>
      </li>
      <li class="contact-item contact-item--address">
        <svg class="contact-icon" viewBox="0 0 24 24" aria-hidden="true">
          <circle cx="12" cy="12" r="10.5" fill="none" stroke="var(--icon-ring)" stroke-width="1"/>
          <path d="M12 5.5a4 4 0 0 0-4 4c0 3 4 7.5 4 7.5s4-4.5 4-7.5a4 4 0 0 0-4-4z" fill="none" stroke="var(--brand-red)" stroke-width="1.2"/>
          <circle cx="12" cy="9.5" r="1.4" fill="var(--brand-red)"/>
        </svg>
        <span>437 Dunmore Lane Suite 12<br>Brenwick CA 90417</span>
      </li>
    </ul>
  </div>

  <svg class="card__band" viewBox="0 0 640 20" preserveAspectRatio="none" aria-hidden="true">
    <polygon points="0,0 316,0 306,20 0,20" fill="var(--brand-red)"/>
    <polygon points="326,0 640,0 640,20 316,20" fill="var(--ink)"/>
  </svg>
</section>

<section class="card card--back" aria-label="Business card back">
  <div class="back__brand brand-name">Zorlivo</div>

  <div class="back__site">
    <svg viewBox="0 0 24 24" aria-hidden="true">
      <g fill="none" stroke="var(--ink)" stroke-width="1.4">
        <circle cx="12" cy="12" r="10"/>
        <ellipse cx="12" cy="12" rx="4.5" ry="10"/>
        <line x1="2" y1="12" x2="22" y2="12"/>
        <line x1="3.5" y1="7" x2="20.5" y2="7"/>
        <line x1="3.5" y1="17" x2="20.5" y2="17"/>
      </g>
    </svg>
    <span>Zorlivo.com</span>
  </div>

  <svg class="card__band" viewBox="0 0 640 20" preserveAspectRatio="none" aria-hidden="true">
    <polygon points="0,0 318,0 308,20 0,20" fill="var(--brand-red)"/>
    <polygon points="328,0 640,0 640,20 318,20" fill="var(--ink)"/>
  </svg>
</section>

</body>
</html>
```